Lodging Venture Advisors

I am an independent operator engaged on short/medium term consultancy briefs within the Hotel/Resort sector in the Pacific Area and have a representation in Fiji.

A broad based services is offered and includes:

Development Advisory
Property Management
Sales & Marketing
Holiday Ownership/Timeshare
Resorts/Apartments/Motels/Flashpackers/B&B
Financial & Legal Referrals

Industry/Entity Type

Hotel

Contact Information for Business Card

Business name - LODGING VENTURE ADVISORS
My name - Grant Whitlock
Address: PO Box 382 Coral Heights 4219 Qld
Phone: Australia: +61 7 55904283 Mobile: 0418952064 (Chatwave)
Fiji: +679 8527319
Email: grantmwhitlock@netmailbox.example

```html
<!DOCTYPE html>
<html lang="en">
<head>
<meta charset="utf-8">
<title>Lodging Venture Advisors – Business Card</title>
<link rel="stylesheet" href="https://fonts.googleapis.com/css2?family=Open+Sans:wght@400;600;700&display=swap">
<style>
  :root{
    --brand-red:#c1272d;
    --ink:#1e1e1e;
    --board-light:#eeeff0;
    --board-dark:#c9cacc;
    --card-edge:#7d7f82;
    --front-light:#fbfbfb;
    --front-mid:#e4e5e6;
    --front-dark:#b9babc;
    --back-strip:#cfd0d2;
    --white:#ffffff;
  }
  html,body{margin:0;padding:0;width:1200px;height:1200px;overflow:hidden;}
  body{
    font-family:"Open Sans",Arial,sans-serif;
    color:var(--ink);
    background:radial-gradient(ellipse at 50% 50%,var(--board-light) 0%,var(--board-light) 35%,var(--board-dark) 100%);
    position:relative;
  }
  .card{
    position:absolute;left:216px;width:762px;height:460px;
    box-sizing:border-box;
    border:1.5px solid var(--card-edge);
    border-radius:0 48px 0 36px;
    overflow:hidden;
  }
  .card--front{
    top:134px;
    background:
      radial-gradient(ellipse 520px 380px at 28% 32%,var(--front-light) 0%,var(--front-mid) 55%,rgba(0,0,0,0) 100%),
      linear-gradient(90deg,var(--front-mid) 0%,var(--front-dark) 100%);
  }
  .card--back{
    top:606px;
    background:linear-gradient(90deg,var(--back-strip) 0px,#e9eaeb 60px,var(--white) 104px,var(--white) 100%);
  }
  .brand{
    position:absolute;display:flex;align-items:center;gap:14px;
    color:var(--brand-red);font-weight:600;
  }
  .brand__mark{width:54px;height:54px;background:var(--brand-red);flex:none;}
  .brand__name{font-size:22px;line-height:23px;letter-spacing:.2px;}
  .card--front .brand{left:60px;top:72px;}
  .card--back .brand{left:300px;top:66px;}

  .services{
    position:absolute;left:0;top:294px;width:762px;
    font-size:18px;line-height:23.5px;
  }
  .services__col{position:absolute;top:0;white-space:nowrap;}
  .services__col--left{right:386px;text-align:right;}
  .services__col--right{left:390px;}
  .services__divider{
    position:absolute;left:379px;top:2px;width:4px;height:104px;background:var(--brand-red);
  }

  .person{
    position:absolute;left:120px;top:234px;margin:0;
    font-size:24px;font-weight:700;
  }
  .contacts{
    position:absolute;left:60px;top:284px;margin:0;padding:0;list-style:none;
    font-size:18px;white-space:nowrap;
  }
  .contacts li{display:flex;align-items:center;height:23.5px;}
  .contacts li.contacts__gap{margin-bottom:9px;}
  .contacts svg{width:20px;height:20px;margin-right:9px;flex:none;}
  .contacts .label{display:inline-block;width:80px;}
</style>
</head>
<body>

<section class="card card--front" aria-label="Card front">
  <div class="brand">
    <span class="brand__mark"></span>
    <span class="brand__name">LODGING<br>VENTURE<br>ADVISORS</span>
  </div>
  <div class="services">
    <div class="services__col services__col--left">Development Advisory<br>Project / Site /<br>Property Management<br>Sales &amp; Marketing</div>
    <span class="services__divider"></span>
    <div class="services__col services__col--right">Holiday Ownership/Timeshare<br>Resorts /Hotels /Apartments /<br>Motels<br>Financial &amp; Legal Referrals</div>
  </div>
</section>

<section class="card card--back" aria-label="Card back">
  <div class="brand">
    <span class="brand__mark"></span>
    <span class="brand__name">LODGING<br>VENTURE<br>ADVISORS</span>
  </div>
  <h1 class="person">Grant Whitlock</h1>
  <ul class="contacts">
    <li class="contacts__gap">
      <svg viewBox="0 0 20 20" aria-hidden="true"><circle cx="10" cy="10" r="10" fill="#f1f1f1"/><rect x="6.5" y="2.5" width="7" height="15" rx="1.5" fill="var(--brand-red)"/><rect x="8" y="4.5" width="4" height="4" fill="#fff"/><circle cx="10" cy="13.5" r="1.2" fill="#fff"/></svg>
      <span>0418 952 064 (Chatwave)</span>
    </li>
    <li>
      <svg viewBox="0 0 20 20" aria-hidden="true"><path d="M10 3 L19 10 H16 V17 H4 V10 H1 Z" fill="var(--brand-red)"/><rect x="8.5" y="12" width="3" height="5" fill="#fff"/></svg>
      <span>PO Box 382 Coral Heights 4219 Qld</span>
    </li>
    <li>
      <svg viewBox="0 0 20 20" aria-hidden="true"><circle cx="10" cy="10" r="10" fill="#f1f1f1"/><path d="M5 4 C3 7 8 15 14 16 L16 13.5 L13 11.5 L11.5 13 C9.5 12 8 10.5 7 8.5 L8.5 7 L6.5 3.5 Z" fill="var(--brand-red)"/></svg>
      <span>Australia: +61 7 5590 4283</span>
    </li>
    <li>
      <svg viewBox="0 0 20 20" aria-hidden="true"><circle cx="10" cy="10" r="10" fill="#f1f1f1"/><rect x="6.5" y="2.5" width="7" height="15" rx="1.5" fill="var(--brand-red)"/><rect x="8" y="4.5" width="4" height="4" fill="#fff"/><circle cx="10" cy="13.5" r="1.2" fill="#fff"/></svg>
      <span class="label">Fiji</span><span>: +679 852 7319 (Chatwave)</span>
    </li>
    <li>
      <svg viewBox="0 0 20 20" aria-hidden="true"><circle cx="10" cy="10" r="10" fill="#f1f1f1"/><rect x="2" y="5" width="16" height="10" rx="1" fill="var(--brand-red)"/><path d="M2.5 5.5 L10 11 L17.5 5.5" fill="none" stroke="#fff" stroke-width="1.4"/></svg>
      <span>grantmwhitlock@netmailbox.example</span>
    </li>
  </ul>
</section>

</body>
</html>
```